Powepoint Templates From Logo

Hello,

I am looking for a template for PowerPoint presentations for a new company selling Brivoxa's. The PowerPoint should keep the look and feel of our newly designed website ( which is still under development ) http://brivoxa.com/development/

I have attached our Logo which should be included in this template.
This PowerPoint will be used towards client during demonstrations and for internal use.

This template should be complete with fonts and colors of the text for both headlines and bullets/normal text.

I guess the easiest way for me to determine what I like is to see some dummy info/text on the submitted designs.

Thanks

Industry/Entity Type

It Company

Requirements
Must have
• Should include our logo

```html
<!DOCTYPE html>
<html lang="en">
<head>
<meta charset="utf-8">
<title>Brivoxa Presentation Template</title>
<link href="https://fonts.googleapis.com/css2?family=Francois+One&family=Roboto+Condensed:wght@400;500&display=swap" rel="stylesheet">
<style>
  :root {
    --green-strong: #7ed321;
    --green-mid: #a8e05a;
    --green-pale: #e6f6d2;
    --white: #ffffff;
    --ink: #111111;
    --grey-text: #6b6b6b;
    --logo-grey: #8a8a8a;
    --rule-green: #9ccc3c;
    --rule-grey: #e2e2e2;
  }
  * { margin: 0; padding: 0; box-sizing: border-box; }
  html, body { width: 1200px; height: 900px; overflow: hidden; background: var(--white); }
  .slide {
    position: relative;
    width: 1200px;
    height: 900px;
    overflow: hidden;
    font-family: "Roboto Condensed", "Arial Narrow", sans-serif;
    color: var(--ink);
    background:
      radial-gradient(ellipse 1100px 860px at 60px 40px,
        var(--green-strong) 0%,
        var(--green-mid) 35%,
        var(--green-pale) 64%,
        rgba(255,255,255,0) 88%),
      var(--white);
  }
  .title {
    position: absolute;
    left: 55px;
    top: 338px;
    font-family: "Francois One", "Arial Narrow", sans-serif;
    font-size: 53px;
    font-weight: 400;
    letter-spacing: 0.2px;
    color: var(--ink);
    text-shadow: 0 3px 4px rgba(0,0,0,0.18);
  }
  .subtext-list {
    position: absolute;
    left: 55px;
    top: 466px;
    list-style: none;
  }
  .subtext-list li {
    font-size: 25px;
    font-weight: 500;
    line-height: 60px;
    color: var(--ink);
  }
  .brand {
    position: absolute;
    left: 758px;
    top: 274px;
    display: flex;
    align-items: center;
    gap: 22px;
  }
  .brand-mark {
    width: 156px;
    height: 156px;
    border-radius: 50%;
    background: var(--green-mid);
  }
  .brand-name {
    font-size: 78px;
    font-weight: 500;
    color: var(--logo-grey);
    letter-spacing: 1px;
  }
  .brand-rule {
    position: absolute;
    left: 740px;
    top: 418px;
    width: 460px;
    height: 2px;
    background: linear-gradient(to right, transparent, var(--rule-grey) 30%, var(--rule-grey) 80%, transparent);
  }
  .product-photo {
    position: absolute;
    left: 892px;
    top: 568px;
    width: 236px;
    height: 140px;
    border-radius: 70px 36px 36px 70px;
    background: radial-gradient(ellipse at 40% 45%, #fdfdfd 0%, #e4e6e8 55%, #c9cccf 100%);
  }
  .footer-rule {
    position: absolute;
    left: 0;
    top: 817px;
    width: 1085px;
    height: 2px;
    background: linear-gradient(to right, rgba(156,204,60,0.2), var(--rule-green));
  }
  .page-number {
    position: absolute;
    left: 1085px;
    top: 787px;
    width: 62px;
    height: 62px;
    border: 2px solid var(--rule-green);
    border-radius: 50%;
    background: var(--white);
    display: flex;
    align-items: center;
    justify-content: center;
    font-family: "Francois One", "Arial Narrow", sans-serif;
    font-size: 26px;
    color: var(--ink);
  }
  .copyright {
    position: absolute;
    left: 47px;
    top: 840px;
    font-size: 23px;
    color: var(--grey-text);
  }
</style>
</head>
<body>
<main class="slide">
  <h1 class="title">Presentation Title Here</h1>

  <ul class="subtext-list">
    <li>Subtext Content Here, Subtext Content Here</li>
    <li>Subtext Content Here, Subtext Content Here</li>
    <li>Subtext Content Here, Subtext Content Here</li>
  </ul>

  <div class="brand">
    <span class="brand-mark" aria-hidden="true"></span>
    <span class="brand-name">Brivoxa</span>
  </div>
  <div class="brand-rule" aria-hidden="true"></div>

  <div class="product-photo" role="img" aria-label="Photo of an LED light bulb with a play button overlay"></div>

  <div class="footer-rule" aria-hidden="true"></div>
  <div class="page-number">01</div>
  <p class="copyright">Copyright@Brivoxa</p>
</main>
</body>
</html>
```